Velvet Saturdays

Nightclub flyer. I'm one of the dj's but I want to do my own flyer for it as well. The night will feature dance/club music but I specialize in house/electronic music. Fall colors would be nice.

Target Market(s)

21-40 year olds who like club/dance/house music. We mainly want to appeal to the ladies

Industry/Entity Type

Club

Requirements
Must have
• VELVET Saturdays

Every Friday

Club Music:

DJQRZ
MOONGLIDER

House Music:

PARAGON
BELLO

123 Drink Specials & $4 Appetizer Specials till Midnight

$1-Draft Special
$2-Shot Special
$3-Well Special

$4-Appetizer Specials

21+
Doors Open @ 9pm
Plenty of FREE Parking

VIP/BIRTHDAYS/GROUPS/INFO
EMAIL: TRELLONIGHTEVENTS@ZUMVEX.COM

Inside Gumbleton's
512 Marlow Ave, Brindlecove 90417
Nice to have
• I really like digital designs of girls like the vox lumea flyers, or outlines of the girls dancing or listening to music with headphones. This isn't mandatory but it's nice to see
Should not have
• While the flyer can feature a pretty, classy girl, I don't want anything too sexy/slutty for the girl. Also I don't like stars or wings.

```html
<!DOCTYPE html>
<html lang="en">
<head>
<meta charset="utf-8">
<title>Velvet Saturdays – Club Night Flyer</title>
<link rel="stylesheet" href="https://fonts.googleapis.com/css2?family=Oswald:wght@600&family=Open+Sans:wght@300;400;600&family=Tinos&display=swap">
<style>
  :root {
    --page: #ffffff;
    --night: #0b0610;
    --deep-purple: #2a0a33;
    --magenta: #c8177a;
    --hot-pink: #ff3fb0;
    --title-pink: #e43aa6;
    --ribbon-dark: #220a26;
    --ribbon-plum: #3a0d3e;
    --white: #ffffff;
    --soft-white: #e9e4ee;
  }
  * { box-sizing: border-box; margin: 0; padding: 0; }
  html, body { width: 1200px; height: 1000px; overflow: hidden; background: var(--page); }
  .canvas { position: relative; width: 1200px; height: 1000px; }

  .flyer {
    position: absolute; left: 323px; top: 0; width: 562px; height: 1000px; overflow: hidden;
    background:
      radial-gradient(ellipse at 50% 20%, rgba(208,24,127,.55), transparent 60%),
      linear-gradient(180deg, #7a1466 0%, var(--deep-purple) 35%, var(--night) 75%, #150a1a 100%);
  }

  .hero-art {
    position: absolute; left: 0; top: 40px; width: 562px; height: 700px;
    background:
      radial-gradient(circle at 33% 30%, rgba(235,190,170,.55) 0 12%, transparent 22%),
      radial-gradient(ellipse at 40% 55%, rgba(205,30,40,.75) 0 14%, transparent 26%),
      radial-gradient(circle at 74% 45%, rgba(20,10,20,.9) 0 18%, rgba(220,40,150,.7) 19% 21%, transparent 23%),
      radial-gradient(circle at 14% 72%, rgba(200,200,215,.55) 0 10%, transparent 16%),
      radial-gradient(circle at 50% 38%, rgba(150,60,170,.5), transparent 60%);
  }

  .date-tab {
    position: absolute; left: 132px; top: 0; width: 330px; height: 64px;
    background: linear-gradient(180deg, #1a1a1a, #000);
    border-bottom: 2px solid rgba(255,255,255,.25);
    color: var(--soft-white); font: 300 40px/64px "Open Sans", sans-serif; text-align: center;
  }

  .title {
    position: absolute; left: 0; width: 562px; text-align: center;
    font-family: "Oswald", sans-serif; font-weight: 600; text-transform: uppercase;
    color: var(--title-pink); line-height: 1; letter-spacing: 2px;
  }
  .title-line-1 { top: 440px; font-size: 132px; }
  .title-line-2 { top: 600px; font-size: 100px; }

  .dj-ribbon {
    position: absolute; left: 70px; top: 752px; width: 460px; height: 40px;
    display: flex; transform: rotate(-4deg);
  }
  .dj-ribbon span {
    display: flex; align-items: center; justify-content: center;
    color: var(--white); font: 600 21px/1 "Open Sans", sans-serif;
  }
  .dj-left { width: 150px; background: var(--magenta); }
  .dj-genre { width: 150px; background: var(--ribbon-dark); }
  .dj-right { width: 160px; background: var(--ribbon-plum); }

  .info-panel {
    position: absolute; left: 102px; top: 805px; width: 376px; height: 195px;
    background: linear-gradient(180deg, rgba(10,5,12,.92), #000);
    color: var(--white); text-align: center;
  }
  .genre-label { color: var(--hot-pink); font: 600 21px/1.1 "Open Sans", sans-serif; margin-top: 4px; }
  .dj-name { font: 400 21px/1.2 "Open Sans", sans-serif; letter-spacing: 1px; }
  .specials-headline { color: var(--hot-pink); font: 400 12.5px/1.5 "Tinos", serif; }
  .age-limit {
    position: absolute; left: 14px; top: 104px; font: 600 24px/1 "Open Sans", sans-serif;
  }
  .specials-list {
    position: absolute; left: 70px; top: 106px; width: 300px; text-align: left;
    font: 400 10px/1.6 "Tinos", serif; text-transform: uppercase;
  }
  .specials-list .indent { padding-left: 72px; }
  .doors { position: absolute; left: 22px; top: 142px; font: 400 12px/1 "Open Sans", sans-serif; }
  .parking { position: absolute; right: 6px; top: 142px; color: var(--hot-pink); font: 400 12px/1 "Open Sans", sans-serif; }
  .contact {
    position: absolute; left: 0; width: 100%; top: 162px; font: 400 9px/1 "Open Sans", sans-serif;
    color: var(--hot-pink);
  }
  .contact b { color: var(--white); font-weight: 400; }
  .venue { position: absolute; left: 0; width: 100%; top: 177px; font: 400 12.5px/1 "Open Sans", sans-serif; }
</style>
</head>
<body>
<div class="canvas">
  <div class="flyer">
    <div class="hero-art" role="img" aria-label="Photo of a dancing woman in a red dress with speakers, a disco ball and shattered glass on a purple backdrop"></div>

    <div class="date-tab">Every Friday</div>

    <div class="title title-line-1">Velvet</div>
    <div class="title title-line-2">Saturdays</div>

    <div class="dj-ribbon">
      <span class="dj-left">DJQRZ</span>
      <span class="dj-genre">Club Music</span>
      <span class="dj-right">MOONGLIDER</span>
    </div>

    <div class="info-panel">
      <p class="genre-label">House Music</p>
      <p class="dj-name">BELLO</p>
      <p class="dj-name">PARAGON</p>
      <p class="specials-headline">123 Drink Specials &amp; $4 Appetizer Specials till Midnight</p>
      <p class="age-limit">21+</p>
      <div class="specials-list">
        <p>$1-Draft Special&nbsp; $2-Shot Special&nbsp; $3-Well Special</p>
        <p class="indent">$4-Appetizer Specials</p>
      </div>
      <p class="doors">Doors Open @ 9pm</p>
      <p class="parking">Plenty of FREE Parking</p>
      <p class="contact">VIP/BIRTHDAYS/GROUPS/INFO EMAIL: <b>TRELLONIGHTEVENTS@ZUMVEX.COM</b></p>
      <p class="venue">Inside Gumbleton's&nbsp;&nbsp;&nbsp; 512 Marlow Ave, Brindlecove 90417</p>
    </div>
  </div>
</div>
</body>
</html>
```